依頼詳細
落ち着いたBARのフライヤーの裏面を作成してください。
表面はロゴだけ印刷します(ロゴは添付ファイル参照ください)
ロゴの世界観を壊さないよう願います。
住所から地図を作成してください。
記載項目
1時間3,000円(税別)
延長 2,500円(税別)
スタッフドリンク 500円~
フード各種 500円~

営業時間 20時~LAST
休日 日曜日・祝日(祝日の前日が日曜日の場合、営業します)
尼崎市柳瀬町4-7-15 ルミエビル2F
電話番号(未定)
サイズ
14.8×10(横書)
ページ数
片面
希望イメージ
シンプル 複雑
単色 カラフル
暗い 明るい
日常 高級
遊び心 厳粛
未来的 伝統的
女性的 男性的
希望する色
グレー系
納品ファイル
• 高解像度JPG (.jpg)
• イラストレーター形式 (.ai)
• フォトショップ形式 (.psd)
• PNG形式 (.png)
補足説明

```html
<!DOCTYPE html>
<html lang="ja">
<head>
<meta charset="utf-8">
<title>BAR MAISON SEPT – Flyer</title>
<link rel="stylesheet" href="https://fonts.googleapis.com/css2?family=Cinzel:wght@400;600&family=Noto+Serif+JP:wght@400;500&display=swap">
<style>
  :root {
    --page: #ffffff;
    --leather-dark: #141414;
    --leather-mid: #2c2b2a;
    --logo-silver: #d9d6cf;
    --ink: #2a2a2a;
    --ink-soft: #555555;
    --label-bg: #3a3a3a;
    --map-fill: #e6e6e6;
    --card-edge: #cfcfcf;
  }
  * { margin: 0; padding: 0; box-sizing: border-box; }
  html, body { width: 843px; height: 1200px; overflow: hidden; background: var(--page); }
  body { position: relative; font-family: "Noto Serif JP", serif; color: var(--ink); }

  .card { position: absolute; left: 28px; width: 787px; height: 553px; }
  .card--front { top: 22px; }
  .card--back { top: 613px; border: 1px solid var(--card-edge); background: var(--page); }

  .leather {
    position: absolute; inset: 0;
    background: radial-gradient(ellipse at 50% 40%, var(--leather-mid) 0%, var(--leather-dark) 75%);
  }
  .front-logo {
    position: absolute; left: 0; right: 0; top: 230px;
    text-align: center; color: var(--logo-silver);
    font-family: "Cinzel", serif; font-weight: 600;
  }
  .front-logo__small { display: block; font-size: 30px; letter-spacing: 8px; margin-bottom: 6px; }
  .front-logo__main { display: block; font-size: 68px; letter-spacing: 5px; line-height: 1; }

  .info { position: absolute; left: 36px; top: 280px; width: 380px; }
  .info__brand { font-family: "Cinzel", serif; font-size: 26px; letter-spacing: 1px; margin-bottom: 20px; color: var(--ink); }
  .info__brand small { font-size: 15px; margin-right: 6px; }
  .hours { font-size: 10px; line-height: 1.9; margin-bottom: 12px; }
  .hours__row { display: flex; align-items: center; gap: 10px; }
  .hours__label {
    display: inline-block; width: 46px; text-align: center;
    background: var(--label-bg); color: #fff;
    font-family: "Cinzel", serif; font-size: 9px; letter-spacing: 1px; line-height: 14px;
  }
  .prices { display: grid; grid-template-columns: 150px 1fr; font-size: 10px; line-height: 1.9; margin-bottom: 12px; }
  .contact { font-size: 10px; line-height: 1.9; color: var(--ink-soft); }

  .map {
    position: absolute; left: 435px; top: 225px; width: 323px; height: 281px;
    background: var(--map-fill);
  }
</style>
</head>
<body>
  <section class="card card--front">
    <div class="leather" role="img" aria-label="Dark black leather texture background"></div>
    <h1 class="front-logo">
      <span class="front-logo__small">BAR</span>
      <span class="front-logo__main">MAISON SEPT</span>
    </h1>
  </section>

  <section class="card card--back">
    <div class="info">
      <h2 class="info__brand"><small>BAR</small>MAISON SEPT</h2>
      <div class="hours">
        <div class="hours__row"><span class="hours__label">OPEN</span><span>20:00～LAST</span></div>
        <div class="hours__row"><span class="hours__label">CLOSE</span><span>日曜・祝日（祝日の前日が日曜日の場合、営業します）</span></div>
      </div>
      <div class="prices">
        <span>1時間：3,000円（税別）</span><span>スタッフドリンク：500円～</span>
        <span>延長：2,500円（税別）</span><span>フード各種：500円～</span>
      </div>
      <div class="contact">
        <p>兵庫県尼崎市柳瀬町4-7-15 ルミエビル2F</p>
        <p>電話番号 06-0000-4821</p>
      </div>
    </div>
    <div class="map" role="img" aria-label="Street map showing the route to the bar"></div>
  </section>
</body>
</html>
```